Faris Methani Business Card

I would like an elegant business card design in both english and arabic.

Ideally a logo design with my name in Arabic (could be a tiger for example)

It should have my Name : Faris Methani
Title: Advisor / Investor
Tel. UAE +971 558 274 903
UK +44 7821 560 287
Email. farmethani412@mailvane.net

I am an active angle investor and have many business interests in the TMT space and invest globally, the design needs to be fresh, elegant and striking.

The design should be catching and grab one's attention when they view the card.

Front card should be in English and Reverse in Arabic....

Target Market(s)

Global Investors, CEO's

Industry/Entity Type

Business

Contact Information for Business Card

Title: Advisor / Investor
Tel. UAE +971 558 274 903
UK +44 7821 560 287

Font styles to use
Serif
Other font styles liked:
• Palantino

Requirements
Must have
• A striking design with a play of my name in Arabic, could be my name that is designed as a tiger for example

```html
<!DOCTYPE html>
<html lang="en">
<head>
<meta charset="utf-8">
<title>Faris Methani – Business Card</title>
<link rel="stylesheet" href="https://fonts.googleapis.com/css2?family=Gelasio:wght@400;600&family=Noto+Naskh+Arabic:wght@400;600&display=swap">
<style>
  :root {
    --page: #e9e7ec;
    --card-purple: #5b2373;
    --card-violet: #4d3d92;
    --card-magenta: #8c2a6c;
    --card-grey: #8d8691;
    --accent-blue: #1f9bd8;
    --accent-green: #b5d334;
    --logo-ink: #efe6f3;
    --title-ink: #d9cde3;
    --shadow: rgba(40, 20, 60, 0.25);
  }
  * { box-sizing: border-box; margin: 0; padding: 0; }
  html, body {
    width: 1200px; height: 873px; overflow: hidden;
    background: var(--page);
  }
  .stage {
    width: 1200px; height: 873px;
    display: flex; flex-direction: column;
    align-items: center; justify-content: center; gap: 34px;
  }
  .card {
    position: relative;
    width: 680px; height: 388px;
    background: var(--card-purple);
    overflow: hidden;
    box-shadow: 0 14px 30px var(--shadow);
    font-family: "Gelasio", "Palatino Linotype", serif;
  }
  .card-backdrop { position: absolute; inset: 0; width: 100%; height: 100%; }
  .brand-chip {
    position: absolute; left: 36px; top: 34px;
    width: 18px; height: 18px; background: var(--logo-ink); border-radius: 2px;
  }
  .logo {
    position: absolute; left: 300px; top: 40px;
    display: flex; align-items: center; gap: 12px;
  }
  .logo-circle {
    width: 52px; height: 52px; border-radius: 50%;
    border: 2px solid var(--logo-ink);
  }
  .logo-name { color: var(--logo-ink); font-size: 21px; font-weight: 400; letter-spacing: 0.5px; }
  .contacts {
    position: absolute; left: 36px; top: 90px;
    color: var(--accent-blue); font-size: 15px; line-height: 1.5;
    font-style: normal;
  }
  .contacts .label { display: inline-block; width: 40px; }
  .identity { position: absolute; left: 390px; top: 222px; right: 0; }
  .identity-name {
    color: var(--accent-blue); font-size: 28px; font-weight: 400;
    padding-left: 8px; padding-bottom: 2px; line-height: 1.2;
  }
  .identity-rule { height: 3px; background: var(--accent-blue); }
  .identity-title { color: var(--title-ink); font-size: 15px; padding: 6px 0 0 10px; }

  /* Reverse side (Arabic) */
  .card-reverse { font-family: "Noto Naskh Arabic", "Gelasio", serif; }
  .card-reverse .logo-circle { border-color: var(--accent-green); }
  .card-reverse .logo-name { color: var(--accent-green); font-size: 22px; }
  .card-reverse .brand-chip { left: 150px; }
  .card-reverse .contacts {
    left: 150px; top: 84px; color: var(--accent-blue); font-size: 15px;
    direction: rtl; text-align: left; line-height: 1.6;
  }
  .card-reverse .contacts .num { direction: ltr; unicode-bidi: embed; font-family: "Gelasio", serif; }
  .card-reverse .contacts .label { width: auto; margin-left: 10px; }
  .card-reverse .identity { direction: rtl; }
  .card-reverse .identity-name { font-size: 26px; padding-right: 10px; padding-left: 0; }
  .card-reverse .identity-rule { background: var(--accent-green); }
  .card-reverse .identity-title { padding: 4px 10px 0 0; }
</style>
</head>
<body>
<main class="stage">
  <article class="card card-front" lang="en">
    <svg class="card-backdrop" viewBox="0 0 680 388" aria-hidden="true">
      <circle cx="-55" cy="527" r="388" fill="var(--card-violet)" opacity="0.85"/>
      <circle cx="694" cy="291" r="208" fill="var(--card-magenta)" opacity="0.75"/>
      <circle cx="97" cy="-83" r="208" fill="none" stroke="#6d3a86" stroke-width="2" opacity="0.6"/>
    </svg>
    <span class="brand-chip" aria-hidden="true"></span>
    <div class="logo">
      <span class="logo-circle" aria-hidden="true"></span>
      <span class="logo-name">Faris Methani</span>
    </div>
    <address class="contacts">
      <div><span class="label">UAE</span>+971 558 274 903</div>
      <div><span class="label">UK</span>+44 7821 560 287</div>
      <div>farmethani412@mailvane.net</div>
    </address>
    <section class="identity">
      <h1 class="identity-name">Faris Methani</h1>
      <div class="identity-rule"></div>
      <p class="identity-title">Advisor / Investor</p>
    </section>
  </article>

  <article class="card card-reverse" lang="ar">
    <svg class="card-backdrop" viewBox="0 0 680 388" aria-hidden="true">
      <path d="M0 0 H120 C90 140 150 290 330 388 H0 Z" fill="var(--card-grey)"/>
      <path d="M120 0 C100 120 150 250 290 388 H330 C150 290 90 140 120 0 Z" fill="#6b4a7d" opacity="0.7"/>
      <circle cx="560" cy="250" r="150" fill="none" stroke="#6d3a86" stroke-width="2" opacity="0.6"/>
    </svg>
    <span class="brand-chip" aria-hidden="true"></span>
    <div class="logo">
      <span class="logo-circle" aria-hidden="true"></span>
      <span class="logo-name">فارس ميثاني</span>
    </div>
    <address class="contacts">
      <div><span class="label">الإمارات</span><span class="num">+971 558 274 903</span></div>
      <div><span class="label">المملكة المتحدة</span><span class="num">+44 7821 560 287</span></div>
      <div><span class="num">farmethani412@mailvane.net</span></div>
    </address>
    <section class="identity">
      <h2 class="identity-name">فارس ميثاني</h2>
      <div class="identity-rule"></div>
      <p class="identity-title">مستشار / مستثمر</p>
    </section>
  </article>
</main>
</body>
</html>
```